Fast Business Card Project

I need a business card with the name RENATO DUARTE stylized on one side and my email on the other (renatocosta4711@mailnova.com)

Industry/Entity Type

Business

Contact Information for Business Card

www.trilhamar.com.br

```html
<!DOCTYPE html>
<html lang="en">
<head>
<meta charset="utf-8">
<title>Renato Duarte – Business Card</title>
<link href="https://fonts.googleapis.com/css2?family=Open+Sans:wght@400;700&display=swap" rel="stylesheet">
<style>
  :root {
    --stage: #a3c1e3;
    --front-deep: #465b7a;
    --front-light: #647d9f;
    --back-paper: #f1f2f4;
    --back-shade: #e2e5ea;
    --ink-white: #ffffff;
    --ink-blue: #2f5e8e;
    --ink-teal: #4caf9e;
  }
  * { margin: 0; padding: 0; box-sizing: border-box; }
  html, body {
    width: 1200px;
    height: 600px;
    overflow: hidden;
    background: var(--stage);
  }
  .canvas {
    width: 1200px;
    height: 600px;
    display: flex;
    align-items: center;
    justify-content: space-evenly;
    font-family: "Open Sans", Arial, sans-serif;
  }
  .card {
    position: relative;
    width: 490px;
    height: 280px;
    overflow: hidden;
    box-shadow: 0 10px 24px rgba(40, 70, 110, 0.25);
  }
  .card-pattern {
    position: absolute;
    inset: 0;
  }
  .card--front .card-pattern {
    background: linear-gradient(135deg, var(--front-light) 0%, var(--front-deep) 55%, var(--front-light) 100%);
  }
  .card--back .card-pattern {
    background: linear-gradient(135deg, var(--back-paper) 0%, var(--back-shade) 50%, var(--back-paper) 100%);
  }
  .front-name {
    position: absolute;
    right: 34px;
    bottom: 34px;
    color: var(--ink-white);
    font-weight: 700;
    font-size: 32px;
    letter-spacing: 0.5px;
  }
  .back-details {
    position: absolute;
    left: 40px;
    bottom: 40px;
  }
  .back-name {
    color: var(--ink-blue);
    font-weight: 700;
    font-size: 36px;
    letter-spacing: 0.5px;
    line-height: 1.1;
  }
  .back-email {
    display: flex;
    align-items: center;
    gap: 10px;
    margin-top: 8px;
    color: var(--ink-blue);
    font-weight: 400;
    font-size: 19px;
  }
  .email-icon { width: 30px; height: 24px; flex: none; }
</style>
</head>
<body>
<main class="canvas">
  <section class="card card--front">
    <div class="card-pattern" role="img" aria-label="Dark blue low-poly geometric texture"></div>
    <p class="front-name">RENATO DUARTE</p>
  </section>

  <section class="card card--back">
    <div class="card-pattern" role="img" aria-label="Faint light grey low-poly geometric texture"></div>
    <div class="back-details">
      <p class="back-name">RENATO DUARTE</p>
      <p class="back-email">
        <svg class="email-icon" viewBox="0 0 30 24" aria-hidden="true">
          <rect x="0" y="0" width="30" height="24" fill="var(--ink-teal)"/>
          <polyline points="0,0 15,13 30,0" fill="none" stroke="#ffffff" stroke-width="2"/>
          <polyline points="0,24 11,10" fill="none" stroke="#ffffff" stroke-width="1.5"/>
          <polyline points="30,24 19,10" fill="none" stroke="#ffffff" stroke-width="1.5"/>
        </svg>
        renatocosta4711@mailnova.com
      </p>
    </div>
  </section>
</main>
</body>
</html>
```